Logo & Web Design for Technical Research Products

Logo and Web Design for a little business selling some niche research, technical products. Current site is at: http://ferrowick.com/ferrowick-battery-test-cell. The audience are university researchers, technical labs and similar.

We would like a more professional looking logo and design than what is currently there.

This new design should include/consider:
- A front page with the ability to show-case 2-3 select products
- An About Us page
- A Contact Us page
- An FAQ page
- A hierarchical menu structure (preferably to the left) allowing for at least two levels. (We plan to add more products and categories in the future)
- Include both a Desktop and Phone version (responsive design)
- We plan to have all products follow a similar template so please have that in mind when desiging (Some part of the product template may be omitted for some products if not applicable)
- Multiple images per product should be supported(carousel perhaps?)

When creating the CSS and HTML please use Bootstap 4.
(https://getplinthkit.com/docs/4.0/getting-started/introduction/)

```html
<!DOCTYPE html>
<html lang="en">
<head>
<meta charset="utf-8">
<title>Ferrowick – Battery Test Cell</title>
<link rel="stylesheet" href="https://fonts.googleapis.com/css2?family=Raleway:wght@400;500;600;700&family=Source+Sans+3:wght@400;600;700&family=Arimo:wght@400&display=swap">
<style>
:root{
  --blue:#1ba3dc;
  --blue-deep:#1678c2;
  --blue-btn:#1984c7;
  --ink:#1d1d1d;
  --grey-text:#4a4a4a;
  --field:#ebebeb;
  --soft:#f2f2f2;
  --white:#ffffff;
  --star:#f5a800;
}
*{box-sizing:border-box;margin:0;padding:0}
html,body{width:1200px;height:3299px;overflow:hidden}
body{position:relative;font-family:"Raleway",sans-serif;color:var(--ink);background:var(--white)}
.abs{position:absolute}
.logo{font-family:"Raleway",sans-serif;font-weight:700;font-size:38px;letter-spacing:.5px}

/* header */
.site-header{position:absolute;left:0;top:0;width:1200px;height:90px;display:flex;align-items:center;justify-content:center}
.main-nav{position:absolute;left:0;top:90px;width:1200px;height:69px;background:var(--blue);display:flex;align-items:center;justify-content:center;gap:20px}
.main-nav a{color:var(--white);text-decoration:none;font-family:"Source Sans 3",sans-serif;font-weight:700;font-size:15.5px;letter-spacing:.1px}
.main-nav a:last-child{margin-left:4px}
.contact-strip{position:absolute;left:0;top:159px;width:1200px;height:73px}
.strip-item{position:absolute;top:17px;display:flex;align-items:center;gap:14px;font-family:"Raleway",sans-serif;font-size:16px;color:#333}
.strip-icon{width:38px;height:36px;border:2px solid var(--blue);display:flex;align-items:center;justify-content:center}

/* hero */
.hero{position:absolute;left:0;top:232px;width:1200px;height:620px;background:linear-gradient(120deg,#2a8fd2 0%,#1e86cc 45%,#2b9ae0 100%);overflow:hidden}
.hero-photo{position:absolute;left:51px;top:37px;width:360px;height:500px;background:radial-gradient(ellipse at 50% 50%,#9fb1c4 0%,#6e87a5 55%,rgba(30,134,204,0) 72%)}
.hero-title{position:absolute;left:475px;top:166px;width:610px;text-align:right;color:var(--white);font-weight:700;font-size:45px}
.hero-text{position:absolute;left:475px;top:232px;width:613px;text-align:right;color:var(--white);font-weight:600;font-size:19px;line-height:30px}
.hero-btn{position:absolute;left:899px;top:328px;width:188px;height:56px;background:var(--white);color:var(--blue-deep);font-weight:600;font-size:26px;display:flex;align-items:center;justify-content:center}
.hero-wave{position:absolute;left:0;bottom:0}

/* about */
.about-title{left:118px;top:902px;font-size:42px;font-weight:700}
.about-text{left:118px;top:982px;width:547px;font-family:"Arimo",sans-serif;font-size:17px;line-height:30px;text-align:justify;color:#222}
.btn-read{left:122px;top:1228px;width:166px;height:53px;background:var(--blue-btn);color:var(--white);font-family:"Source Sans 3",sans-serif;font-size:20px;display:flex;align-items:center;justify-content:center;gap:16px}
.photo{position:absolute}

/* products */
.products{position:absolute;left:0;top:1377px;width:1200px;height:666px;background:var(--soft)}
.section-title{position:absolute;left:0;width:1200px;text-align:center;font-weight:700;font-size:40px;color:#4a4a4a}
.card{position:absolute;top:174px;width:284px;height:410px;border:2px solid var(--blue-deep);background:rgba(255,255,255,.25)}
.card-photo{position:absolute;left:50px;top:10px;width:184px;height:232px;border-radius:6px}
.card-name{position:absolute;left:0;top:248px;width:100%;text-align:center;font-weight:700;font-size:22px;color:#222}
.card-stars{position:absolute;left:0;top:284px;width:100%;display:flex;justify-content:center;gap:10px}
.card-price{position:absolute;left:0;top:324px;width:100%;text-align:center;font-family:"Source Sans 3",sans-serif;font-weight:700;font-size:22px;color:#222}
.card-buy{position:absolute;left:76px;top:374px;width:132px;height:45px;background:var(--blue-btn);color:var(--white);font-family:"Source Sans 3",sans-serif;font-weight:700;font-size:14px;display:flex;align-items:center;justify-content:center}
.slider-arrow{position:absolute;top:314px;width:52px;height:52px}

/* newsletter */
.newsletter{position:absolute;left:0;top:2043px;width:1200px;height:175px;background:linear-gradient(100deg,#8fcfee 0%,#3aa9e2 40%,#1b95d9 100%)}
.newsletter-title{position:absolute;left:228px;top:69px;color:var(--white);font-weight:700;font-size:33px}
.newsletter-form{position:absolute;left:693px;top:64px;width:370px;height:52px;background:var(--white);border-radius:26px;border:2px solid var(--white)}
.newsletter-form span{position:absolute;left:34px;top:14px;font-size:16px;color:#8a8a8a}
.newsletter-form b{position:absolute;right:0;top:0;width:138px;height:48px;border-radius:24px;background:var(--blue-btn);color:var(--white);font-family:"Source Sans 3",sans-serif;font-weight:600;font-size:17px;display:flex;align-items:center;justify-content:center}

/* contact */
.field{position:absolute;background:var(--field);font-size:18px;color:#555;padding:22px 0 0 48px}
.field.msg{padding-left:48px}
.send-btn{left:542px;top:2844px;width:116px;height:41px;background:var(--blue);color:var(--white);font-size:18px;display:flex;align-items:center;justify-content:center}

/* footer */
.site-footer{position:absolute;left:0;top:2949px;width:1200px;height:350px;background:linear-gradient(110deg,#4fb6e6 0%,#2aa2de 45%,#1a8ed4 100%);color:var(--white)}
.footer-logo{position:absolute;left:0;top:54px;width:1200px;text-align:center}
.footer-links{position:absolute;left:0;top:132px;width:1200px;display:flex;justify-content:center;gap:18px;font-family:"Source Sans 3",sans-serif;font-size:21px}
.footer-contact{position:absolute;left:0;top:184px;width:1200px;display:flex;justify-content:center;gap:38px;font-family:"Source Sans 3",sans-serif;font-size:17px}
.footer-contact span{display:flex;align-items:center;gap:12px}
.footer-social{position:absolute;left:0;top:240px;width:1200px;display:flex;justify-content:center;gap:20px}
.footer-social i{width:22px;height:22px;border-radius:50%;border:2px solid var(--white)}
.footer-rule{position:absolute;left:0;top:294px;width:1200px;height:1px;background:rgba(255,255,255,.45)}
.footer-copy{position:absolute;left:108px;top:315px;font-family:"Source Sans 3",sans-serif;font-size:13px}
</style>
</head>
<body>

<header class="site-header"><span class="logo">Ferrowick</span></header>

<nav class="main-nav">
  <a>BATTERY TESTER</a>
  <a>FERROWICK BATTERY TEST CELL</a>
  <a>PHOTOELECTROCHEMICAL TEST CELL</a>
  <a>2 CHANNEL PERISTALTIC PUMP</a>
  <a>CONTACT US</a>
</nav>

<div class="contact-strip">
  <div class="strip-item" style="left:668px">
    <span class="strip-icon"><svg width="22" height="16" viewBox="0 0 22 16"><rect x="1" y="1" width="20" height="14" fill="#222"/><path d="M1 1l10 8 10-8" stroke="#fff" stroke-width="1.6" fill="none"/></svg></span>
    sales@ferrowick.com
  </div>
  <div class="strip-item" style="left:924px">
    <span class="strip-icon"><svg width="20" height="20" viewBox="0 0 24 24"><path d="M6.6 10.8a15 15 0 006.6 6.6l2.2-2.2c.3-.3.7-.4 1-.2 1.1.4 2.3.6 3.6.6.6 0 1 .4 1 1V20c0 .6-.4 1-1 1A17 17 0 013 4c0-.6.4-1 1-1h3.5c.6 0 1 .4 1 1 0 1.3.2 2.5.6 3.6.1.3 0 .7-.2 1z" fill="#222"/></svg></span>
    888 888 8888
  </div>
</div>

<section class="hero">
  <div class="hero-photo" role="img" aria-label="Photo of the battery test cell: stacked aluminium plates with blue tube fittings"></div>
  <h1 class="hero-title">Ferrowick Battery Test Cell</h1>
  <p class="hero-text">Lorem ipsum dolor sit amet, consectetur adipiscing elit, sed do eiusmod tempor incididunt ut labore et dolore magna aliqua. Quis</p>
  <div class="hero-btn">Buy Now</div>
  <svg class="hero-wave" width="1200" height="120" viewBox="0 0 1200 120">
    <path d="M0 75 C250 35 500 45 700 85 C900 122 1100 105 1200 80 L1200 120 L0 120Z" fill="#fff"/>
    <path d="M620 83 C850 120 1080 110 1200 76 L1200 82 C1080 118 850 130 620 83Z" fill="#000"/>
  </svg>
</section>

<h2 class="abs about-title">About Us</h2>
<p class="abs about-text">Lorem Ipsum is simply dummy text of the printing and typesetting industry. Lorem Ipsum has been the industry’s standard dummy text ever since the 1500s, when an unknown printer took a galley of type and scrambled it to make a type specimen book. It has survived not only five centuries, but also the leap into electronic typesetting, remaining essentially unchanged. It was popularised in the 1960s with the release of Letraset sheets</p>
<div class="abs btn-read">Read More
  <svg width="24" height="16" viewBox="0 0 24 16"><path d="M0 0l11 8-11 8zM12 0l11 8-11 8z" fill="#fff"/></svg>
</div>
<div class="photo" style="left:766px;top:920px;width:305px;height:128px;background:linear-gradient(180deg,#eeeeee,#c9cbcd)" role="img" aria-label="Photo of a rack-mount multi-channel battery tester"></div>
<div class="photo" style="left:748px;top:1058px;width:137px;height:242px;background:linear-gradient(180deg,#d9dde0,#a9b0b6)" role="img" aria-label="Photo of a battery tester cabinet in a lab"></div>
<div class="photo" style="left:898px;top:1058px;width:192px;height:242px;background:linear-gradient(160deg,#6c8f7a,#3b8a5a 50%,#88a090)" role="img" aria-label="Photo of test channels with green indicator lights"></div>

<section class="products">
  <h2 class="section-title" style="top:64px">Our Products</h2>

  <svg class="slider-arrow" style="left:48px" viewBox="0 0 52 52"><circle cx="26" cy="26" r="24" fill="none" stroke="#1678c2" stroke-width="2.5"/><path d="M36 26H17M25 18l-8 8 8 8" stroke="#1678c2" stroke-width="3.5" fill="none"/></svg>
  <svg class="slider-arrow" style="left:1098px" viewBox="0 0 52 52"><circle cx="26" cy="26" r="24" fill="none" stroke="#1678c2" stroke-width="2.5"/><path d="M16 26h19M27 18l8 8-8 8" stroke="#1678c2" stroke-width="3.5" fill="none"/></svg>

  <div class="card" style="left:132px">
    <div class="card-photo" style="background:linear-gradient(180deg,#c8cbcf,#5b6068)" role="img" aria-label="Photo of a peristaltic pump with display"></div>
    <div class="card-name">Lorem Ipsum</div>
    <div class="card-stars"><svg width="132" height="24" viewBox="0 0 132 24"><g fill="#f5a800"><path id="st" d="M12 1l3.3 7 7.7.9-5.7 5.2 1.6 7.6L12 17.8 5.1 21.7l1.6-7.6L1 8.9l7.7-.9z"/><use href="#st" x="34"/><use href="#st" x="68"/><use href="#st" x="102"/></g></svg></div>
    <div class="card-price">$ 35.6</div>
    <div class="card-buy">BUY NOW</div>
  </div>

  <div class="card" style="left:457px">
    <div class="card-photo" style="background:linear-gradient(180deg,#b7c3cf,#5e86b8)" role="img" aria-label="Photo of the battery test cell"></div>
    <div class="card-name">Lorem Ipsum</div>
    <div class="card-stars"><svg width="132" height="24" viewBox="0 0 132 24"><g fill="#f5a800"><use href="#st"/><use href="#st" x="34"/><use href="#st" x="68"/><use href="#st" x="102"/></g></svg></div>
    <div class="card-price">$ 19.6</div>
    <div class="card-buy">BUY NOW</div>
  </div>

  <div class="card" style="left:782px">
    <div class="card-photo" style="background:linear-gradient(180deg,#d2d4d6,#3a3d42)" role="img" aria-label="Photo of a photoelectrochemical test cell"></div>
    <div class="card-name">Lorem Ipsum</div>
    <div class="card-stars"><svg width="132" height="24" viewBox="0 0 132 24"><g fill="#f5a800"><use href="#st"/><use href="#st" x="34"/><use href="#st" x="68"/><use href="#st" x="102"/></g></svg></div>
    <div class="card-price">$ 39.6</div>
    <div class="card-buy">BUY NOW</div>
  </div>
</section>

<section class="newsletter">
  <svg class="abs" style="left:138px;top:65px" width="63" height="48" viewBox="0 0 63 48"><rect x="2" y="2" width="59" height="44" fill="none" stroke="#fff" stroke-width="4"/><path d="M2 2l29.5 24L61 2M2 46l22-22M61 46L39 24" stroke="#fff" stroke-width="4" fill="none"/></svg>
  <div class="newsletter-title">Subscribe To Newsletter</div>
  <div class="newsletter-form"><span>Enter Email Address</span><b>SUBSCRIBE</b></div>
</section>

<h2 class="section-title" style="top:2287px">Contact Us</h2>
<div class="field" style="left:159px;top:2394px;width:401px;height:71px">Name</div>
<div class="field" style="left:640px;top:2394px;width:401px;height:71px;padding-left:40px">Last Name</div>
<div class="field" style="left:159px;top:2488px;width:401px;height:71px">Email</div>
<div class="field" style="left:640px;top:2488px;width:401px;height:71px;padding-left:40px">Phone</div>
<div class="field msg" style="left:159px;top:2592px;width:880px;height:205px">Message</div>
<div class="abs send-btn">Send</div>

<footer class="site-footer">
  <div class="footer-logo"><span class="logo">Ferrowick</span></div>
  <div class="footer-links"><span>Home</span><span>/</span><span>About</span><span>/</span><span>Contact Us</span></div>
  <div class="footer-contact">
    <span><svg width="22" height="22" viewBox="0 0 24 24"><path d="M6.6 10.8a15 15 0 006.6 6.6l2.2-2.2c.3-.3.7-.4 1-.2 1.1.4 2.3.6 3.6.6.6 0 1 .4 1 1V20c0 .6-.4 1-1 1A17 17 0 013 4c0-.6.4-1 1-1h3.5c.6 0 1 .4 1 1 0 1.3.2 2.5.6 3.6.1.3 0 .7-.2 1z" fill="#fff"/></svg>888 8888 8888</span>
    <span><svg width="28" height="20" viewBox="0 0 28 20"><rect x="1" y="1" width="26" height="18" fill="none" stroke="#fff" stroke-width="2"/><path d="M1 1l13 10L27 1M1 19l10-9M27 19l-10-9" stroke="#fff" stroke-width="2" fill="none"/></svg>sales@ferrowick.com</span>
    <span><svg width="16" height="22" viewBox="0 0 16 22"><path d="M8 0a8 8 0 00-8 8c0 6 8 14 8 14s8-8 8-14a8 8 0 00-8-8z" fill="#fff"/><circle cx="8" cy="8" r="3" fill="#2aa2de"/></svg>Lorem ipsum dol sit</span>
  </div>
  <div class="footer-social"><i></i><i></i><i></i><i></i></div>
  <div class="footer-rule"></div>
  <div class="footer-copy">© 2019 All Rights Reserved | Privacy Policy | Terms and Conditions</div>
</footer>

</body>
</html>
```